Crafted Ember Website

Would like a website designed for my fitness and nutrition coaching company Craft Ember. I have a company logo and would like to keep the page layout clean and simple. Needs to look great on computer and mobile devices.

Target Market(s)

Target market is individuals looking to make changes in their health and nutrition with the help of an online coach.

Industry/Entity Type

Fitness

Number of Pages Required

2 page

Colors
3176b5
0355a3
85acd3
cedeed
f8fcfd
ffffff

Requirements
Must have
• The first page should have the company logo and name towards the top and below that client before and after photos scrolling or displaying in some manner. Also would like a section that states services offered and a section about myself since I am the primary coach for clients.

```html
<!DOCTYPE html>
<html lang="en">
<head>
<meta charset="utf-8">
<title>Crafted Ember – Fitness &amp; Nutrition Coaching</title>
<link rel="stylesheet" href="https://fonts.googleapis.com/css2?family=Open+Sans:ital,wght@0,400;0,600;0,700;0,800;1,400&display=swap">
<style>
  :root {
    --blue: #3176b5;
    --navy: #0355a3;
    --sky: #85acd3;
    --band: #7a9dcb;
    --mist: #cedeed;
    --snow: #f8fcfd;
    --white: #ffffff;
    --ink: #3a3a3a;
    --muted: #8a8a8a;
    --grey-bg: #f5f5f5;
    --heading-grey: #7b7b7b;
  }
  * { box-sizing: border-box; margin: 0; padding: 0; }
  html, body { width: 1200px; height: 3396px; overflow: hidden; }
  body { font-family: "Open Sans", Arial, sans-serif; color: var(--ink); background: var(--white); position: relative; }
  section, header, footer { position: absolute; left: 0; width: 1200px; }

  /* Header */
  .site-header { top: 0; height: 118px; background: var(--white); }
  .brand { position: absolute; left: 96px; top: 36px; display: flex; align-items: center; gap: 12px; }
  .brand-mark { width: 30px; height: 30px; background: var(--navy); }
  .brand-name { font-size: 24px; font-weight: 700; color: var(--navy); letter-spacing: 0.5px; }
  .main-nav { position: absolute; right: 98px; top: 52px; display: flex; gap: 50px; }
  .main-nav a { font-size: 13px; font-weight: 600; color: #666; text-decoration: none; letter-spacing: 0.5px; padding-bottom: 12px; }
  .main-nav a.active { color: var(--blue); border-bottom: 2px solid var(--blue); }

  /* Hero */
  .hero { top: 118px; height: 606px; overflow: hidden; }
  .hero-photo { position: absolute; inset: 0; background: linear-gradient(180deg, #8fa8b8 0%, #c9b6a0 38%, #e8c28e 52%, #8d8a86 70%, #5d5a58 100%); }
  .hero-title { position: absolute; top: 196px; width: 100%; text-align: center; font-size: 82px; font-weight: 800; color: var(--white); letter-spacing: 1px; line-height: 1; text-shadow: 0 3px 8px rgba(0,0,0,.35); }
  .hero-tagline { position: absolute; top: 282px; width: 100%; text-align: center; font-size: 28px; color: var(--white); text-shadow: 0 2px 6px rgba(0,0,0,.35); }
  .hero-btn { position: absolute; left: 516px; top: 342px; width: 168px; height: 43px; background: var(--navy); color: var(--white); font-size: 15px; font-weight: 600; display: flex; align-items: center; justify-content: center; }
  .slider-arrow { position: absolute; top: 282px; width: 44px; height: 44px; border-radius: 50%; background: rgba(255,255,255,.25); display: flex; align-items: center; justify-content: center; }
  .slider-arrow.prev { left: 24px; }
  .slider-arrow.next { right: 24px; }

  /* Before / after */
  .transformations { top: 724px; height: 358px; background: var(--band); }
  .result-card { position: absolute; top: 64px; width: 317px; height: 220px; background: var(--white); }
  .result-labels { height: 41px; display: flex; }
  .result-labels span { flex: 1; text-align: center; line-height: 41px; font-size: 16px; font-weight: 700; color: #222; }
  .result-photos { display: flex; height: 179px; }
  .result-photo { flex: 1; }
  .photo-a { background: linear-gradient(160deg, #b8a48f, #6d7d86); }
  .photo-b { background: linear-gradient(160deg, #c7d3dc, #9a8a7a); }
  .photo-c { background: linear-gradient(160deg, #e8dbd0, #b99780); }
  .photo-d { background: linear-gradient(160deg, #eceae8, #b89580); }
  .photo-e { background: linear-gradient(160deg, #dbd7d5, #9a8c90); }
  .photo-f { background: linear-gradient(160deg, #e2dfdd, #a28a8c); }
  .band-arrow { position: absolute; top: 163px; }

  /* Welcome */
  .welcome { top: 1082px; height: 462px; text-align: center; }
  .section-title { font-weight: 700; line-height: 1.2; }
  .welcome .section-title { position: absolute; top: 70px; width: 100%; font-size: 38px; color: var(--navy); }
  .body-copy { font-size: 13px; line-height: 25px; color: var(--muted); }
  .welcome .p1 { position: absolute; top: 142px; left: 160px; width: 880px; }
  .welcome .p2 { position: absolute; top: 236px; left: 160px; width: 880px; }
  .btn-solid { position: absolute; left: 444px; top: 317px; width: 310px; height: 52px; background: var(--navy); color: var(--white); font-size: 17px; font-weight: 600; display: flex; align-items: center; justify-content: center; }

  /* About */
  .about { top: 1544px; height: 426px; text-align: center; overflow: hidden; }
  .about-photo { position: absolute; inset: 0; background: linear-gradient(180deg, #4f7fb9 0%, #3c6ea9 50%, #244f86 100%); }
  .about .section-title { position: absolute; top: 68px; width: 100%; font-size: 64px; font-weight: 400; color: var(--white); }
  .about .body-copy { color: var(--white); font-size: 14px; line-height: 26px; position: absolute; left: 160px; width: 880px; }
  .about .p1 { top: 166px; }
  .about .p2 { top: 266px; }

  /* Services */
  .services { top: 1970px; height: 554px; text-align: center; }
  .services .section-title { position: absolute; top: 56px; width: 100%; font-size: 38px; color: var(--heading-grey); }
  .services .intro { position: absolute; top: 128px; left: 300px; width: 600px; }
  .service { position: absolute; top: 226px; width: 240px; }
  .service-icon { width: 104px; height: 104px; margin: 0 auto; border: 3px solid var(--blue); border-radius: 50%; display: flex; align-items: center; justify-content: center; }
  .service-name { margin-top: 24px; font-size: 15px; font-weight: 600; color: #333; }
  .service-desc { margin-top: 12px; font-size: 12px; line-height: 21px; color: #555; }

  /* Testimonials */
  .testimonials { top: 2524px; height: 566px; background: var(--grey-bg); text-align: center; }
  .testimonials .section-title { position: absolute; top: 62px; width: 100%; font-size: 38px; color: var(--heading-grey); }
  .quote { position: absolute; top: 140px; left: 180px; width: 840px; font-size: 19px; font-style: italic; line-height: 29px; color: #666; }
  .quote-mark { position: absolute; font-size: 90px; color: #ddd; font-family: Georgia, serif; line-height: 1; }
  .quote-mark.open { left: 140px; top: 118px; }
  .quote-mark.close { right: 140px; top: 268px; }
  .avatar { position: absolute; left: 532px; top: 306px; width: 136px; height: 136px; border-radius: 50%; border: 5px solid var(--white); box-shadow: 0 1px 4px rgba(0,0,0,.15); background: radial-gradient(circle at 50% 40%, #e7c6a8, #b98e6e 70%, #8a6a55); }
  .client-name { position: absolute; top: 462px; width: 100%; font-size: 16px; letter-spacing: 1px; color: #666; }
  .testimonials .t-arrow { position: absolute; top: 195px; }

  /* Footer */
  .site-footer { top: 3090px; height: 306px; background: var(--navy); color: var(--white); }
  .footer-heading { position: absolute; top: 50px; font-size: 20px; font-weight: 600; }
  .contact-list { position: absolute; left: 134px; top: 110px; list-style: none; font-size: 14px; }
  .contact-list li { display: flex; align-items: center; gap: 10px; height: 32px; }
  .newsletter-note { position: absolute; left: 654px; top: 98px; font-size: 11px; }
  .newsletter-form { position: absolute; left: 654px; top: 125px; display: flex; }
  .newsletter-input { width: 297px; height: 36px; background: var(--white); color: #aaa; font-size: 12px; letter-spacing: 1px; padding-left: 12px; line-height: 36px; }
  .newsletter-btn { width: 118px; height: 36px; background: var(--blue); font-size: 14px; font-weight: 600; line-height: 36px; text-align: center; }
  .footer-rule { position: absolute; left: 134px; right: 134px; top: 224px; border-top: 1px solid rgba(255,255,255,.25); }
  .copyright { position: absolute; top: 252px; width: 100%; text-align: center; font-size: 12px; }
</style>
</head>
<body>

<header class="site-header">
  <div class="brand">
    <span class="brand-mark"></span>
    <span class="brand-name">CRAFTED EMBER</span>
  </div>
  <nav class="main-nav">
    <a class="active">HOME</a>
    <a>ABOUT US</a>
    <a>OUR SERVICES</a>
    <a>TESTIMONIALS</a>
    <a>CONTACT US</a>
  </nav>
</header>

<section class="hero">
  <div class="hero-photo" role="img" aria-label="Couple jogging along a seaside boardwalk at sunset"></div>
  <h1 class="hero-title">CRAFTED EMBER</h1>
  <p class="hero-tagline">We are a fitness and nutrition coaching company.</p>
  <div class="hero-btn">LEARN MORE &gt;&gt;</div>
  <div class="slider-arrow prev"><svg width="14" height="20" viewBox="0 0 14 20"><path d="M11 2 3 10l8 8" fill="none" stroke="#fff" stroke-width="2.5"/></svg></div>
  <div class="slider-arrow next"><svg width="14" height="20" viewBox="0 0 14 20"><path d="M3 2l8 8-8 8" fill="none" stroke="#fff" stroke-width="2.5"/></svg></div>
</section>

<section class="transformations">
  <svg class="band-arrow" style="left:66px" width="14" height="30" viewBox="0 0 14 30"><path d="M12 2 2 15l10 13" fill="none" stroke="#c5d5ea" stroke-width="2"/></svg>
  <svg class="band-arrow" style="right:66px" width="14" height="30" viewBox="0 0 14 30"><path d="M2 2l10 13L2 28" fill="none" stroke="#c5d5ea" stroke-width="2"/></svg>

  <div class="result-card" style="left:100px">
    <div class="result-labels"><span>Before</span><span>After</span></div>
    <div class="result-photos">
      <div class="result-photo photo-a" role="img" aria-label="Client before photo"></div>
      <div class="result-photo photo-b" role="img" aria-label="Client after photo"></div>
    </div>
  </div>
  <div class="result-card" style="left:441px">
    <div class="result-labels"><span>Before</span><span>After</span></div>
    <div class="result-photos">
      <div class="result-photo photo-c" role="img" aria-label="Client before photo, torso"></div>
      <div class="result-photo photo-d" role="img" aria-label="Client after photo, toned torso"></div>
    </div>
  </div>
  <div class="result-card" style="left:783px">
    <div class="result-labels"><span>Before</span><span>After</span></div>
    <div class="result-photos">
      <div class="result-photo photo-e" role="img" aria-label="Client before photo"></div>
      <div class="result-photo photo-f" role="img" aria-label="Client after photo"></div>
    </div>
  </div>
</section>

<section class="welcome">
  <h2 class="section-title">Welcome to Crafted Ember</h2>
  <p class="body-copy p1">Nemo enim ipsam voluptatem quia voluptas sit aspernatur aut odit aut fugit, sed quia consequuntur magni dolores eos qui ratione voluptatem sequi nesciunt. Neque porro quisquam est, qui dolorem ipsum quia dolor sit amet, consectetur, adipisci velit, sed quia non numquam eius modi tempora incidunt ut labore et dolore magnam aliquam quaerat voluptatem.</p>
  <p class="body-copy p2">Sed ut perspiciatis unde omnis iste natus error sit voluptatem accusantium doloremque laudantium, totam rem aperiam, eaque ipsa quae ab illo inventore veritatis et quasi architecto beatae vitae dicta sunt explicabo.</p>
  <div class="btn-solid">READ MORE INFORMATION</div>
</section>

<section class="about">
  <div class="about-photo" role="img" aria-label="Runner on a grassy field under a blue sky"></div>
  <h2 class="section-title">About Crafted Ember</h2>
  <p class="body-copy p1">Sed ut perspiciatis unde omnis iste natus error sit voluptatem accusantium doloremque laudantium, totam rem aperiam, eaque ipsa quae ab illo inventore veritatis et quasi architecto beatae vitae dicta sunt explicabo. Nemo enim ipsam voluptatem quia voluptas sit aspernatur aut odit aut fugit, sed quia consequuntur magni dolores.</p>
  <p class="body-copy p2">Neque porro quisquam est, qui dolorem ipsum quia dolor sit amet, consectetur, adipisci velit, sed quia non numquam eius modi tempora incidunt ut labore et dolore magnam aliquam quaerat voluptatem.</p>
</section>

<section class="services">
  <h2 class="section-title">Our Services</h2>
  <p class="body-copy intro">Nemo enim ipsam voluptatem quia voluptas sit aspernatur aut odit aut fugit, sed quia consequuntur magni dolores eos qui ratione voluptatem sequi nesciunt.</p>

  <div class="service" style="left:88px">
    <div class="service-icon"><svg width="50" height="46" viewBox="0 0 50 46"><path d="M25 42 6 23C0 17 3 6 12 5c6-1 10 3 13 7 3-4 7-8 13-7 9 1 12 12 6 18z" fill="var(--blue)"/></svg></div>
    <div class="service-name">Nutritional Health</div>
    <p class="service-desc">Sed do eiusmod tempor incididunt ut labore et dolore magna aliqua. Ut enim ad minim veniam, quis nostrud exercitation ullamco laboris.</p>
  </div>
  <div class="service" style="left:349px">
    <div class="service-icon"><svg width="56" height="30" viewBox="0 0 56 30"><rect x="2" y="9" width="6" height="12" fill="var(--blue)"/><rect x="9" y="3" width="7" height="24" fill="var(--blue)"/><rect x="16" y="13" width="24" height="4" fill="var(--blue)"/><rect x="40" y="3" width="7" height="24" fill="var(--blue)"/><rect x="48" y="9" width="6" height="12" fill="var(--blue)"/></svg></div>
    <div class="service-name">Personal Training</div>
    <p class="service-desc">Sed do eiusmod tempor incididunt ut labore et dolore magna aliqua. Ut enim ad minim veniam, quis nostrud exercitation ullamco laboris.</p>
  </div>
  <div class="service" style="left:609px">
    <div class="service-icon"><svg width="48" height="48" viewBox="0 0 48 48"><circle cx="24" cy="24" r="18" fill="none" stroke="var(--blue)" stroke-width="4"/><circle cx="24" cy="24" r="7" fill="var(--blue)"/></svg></div>
    <div class="service-name">Wellness Training</div>
    <p class="service-desc">Sed do eiusmod tempor incididunt ut labore et dolore magna aliqua. Ut enim ad minim veniam, quis nostrud exercitation ullamco laboris.</p>
  </div>
  <div class="service" style="left:869px">
    <div class="service-icon"><svg width="44" height="44" viewBox="0 0 44 44"><path d="M22 4 26 18 40 22 26 26 22 40 18 26 4 22 18 18z" fill="var(--blue)"/></svg></div>
    <div class="service-name">Fitness Training</div>
    <p class="service-desc">Sed do eiusmod tempor incididunt ut labore et dolore magna aliqua. Ut enim ad minim veniam, quis nostrud exercitation ullamco laboris.</p>
  </div>
</section>

<section class="testimonials">
  <h2 class="section-title">Client Testimonials</h2>
  <svg class="t-arrow" style="left:100px" width="14" height="30" viewBox="0 0 14 30"><path d="M12 2 2 15l10 13" fill="none" stroke="#bbb" stroke-width="2"/></svg>
  <svg class="t-arrow" style="right:100px" width="14" height="30" viewBox="0 0 14 30"><path d="M2 2l10 13L2 28" fill="none" stroke="#bbb" stroke-width="2"/></svg>
  <span class="quote-mark open">&ldquo;</span>
  <p class="quote">But I must explain to you how all this mistaken idea of denouncing pleasure and praising pain was born and I will give you a complete account of the system, and expound the actual teachings of the great explorer of the truth, the master-builder of human happiness. No one rejects, dislikes, or avoids pleasure itself, because it is pleasure, but because those who do not know how to pursue pleasure rationally encounter consequences that are extremely painful</p>
  <span class="quote-mark close">&rdquo;</span>
  <div class="avatar" role="img" aria-label="Client portrait"></div>
  <p class="client-name">- ASSUMENDA EST</p>
</section>

<footer class="site-footer">
  <h3 class="footer-heading" style="left:134px">CONTACT US</h3>
  <ul class="contact-list">
    <li><svg width="14" height="14" viewBox="0 0 14 14"><path d="M3 1 5 4 4 6c1 2 2 3 4 4l2-1 3 2-1 2c-6 0-11-5-11-11z" fill="#fff"/></svg>Rosalind - 0198 765 432</li>
    <li><svg width="15" height="12" viewBox="0 0 15 12"><rect x="1" y="1" width="13" height="10" fill="none" stroke="#fff" stroke-width="1.5"/><path d="M1 1l6.5 6L14 1" fill="none" stroke="#fff" stroke-width="1.5"/></svg>Email - hello@craftedember.com</li>
  </ul>
  <h3 class="footer-heading" style="left:654px">SUBSCRIBE YOUR NEWSLETTER</h3>
  <p class="newsletter-note">sign up with your email address to receive news and updates.</p>
  <div class="newsletter-form">
    <div class="newsletter-input">EMAIL ADDRESS</div>
    <div class="newsletter-btn">SUBSCRIBE</div>
  </div>
  <div class="footer-rule"></div>
  <p class="copyright">© 2017 CRAFTED EMBER . ALL RIGHTS RESERVED.</p>
</footer>

</body>
</html>
```